Disability Service Provider Website

We are working with VEO, which provides services and job training designed to educate, facilitate, train, and assist individuals with disabilities. They describe their clients using words like Unity and Unique.
Some sites to use for content/competitors and inspiration:
https://www.skillmora.com
https://www.pbtw.org
https://www.thebridgeofmo.org
https://www.openharbor.org
https://velmorin.org
Thank you for taking the time to consider designing a website for us. We are web developers based in Stockton, CA, USA. Most of our projects go through the same process. Understanding this process may help you win a project with us. We custom-code all of our websites in-house. We don’t have any requirements as to what tools you use for your design, but we prefer Figma files. For any design that we label as four-stars, we send it to the client for review. The client picks the final design they want us to use. Once we complete this process, we will continue to show additional clients all the four-star sites and purchase them later. Your designs will have multiple chances to sell. For better chances of success, we ask that you follow these guidelines.
IMAGES:
If you use any images or icons in the design, we ask that you have a link to the asset so we can purchase the image/icon. Most of the designs we submit do not have the customer’s images on them unless they have some great images. Be creative; show us the feeling you are trying to portray with your image choices. Use any royalty-free site you choose. We subscribe to Adobe and mainly use their images, but we can purchase images outside of Adobe.
PLEASE NOTE: we will not submit designs to clients with watermarks on the images.
FONTS:
We ask that you identify the fonts used in the design. This can be done in a message if you want. We typically use Google Fonts and Adobe Fonts.
CONTENT:
We're always open to different content and ideas. We often submit designs with stock images so the client can see our vision. We typically take pictures after the website launch to use their images with our vision. Lorem Ipsum is fine for paragraphs, but we ask that you write the headers in correct English. We want to be able to show the vision and identify the sections of the website.
INSPIRATION:
We typically add a couple of links in the brief of websites we like to help you get started in your design.
REVISIONS:
We do not often ask for revisions of the designs unless we see something in the design that may not appeal to the client. If there are slight changes that we want to make, we do that in the development process.
FEEDBACK:
We rarely give feedback on designs during the design process. We are working on many website projects and do not have the time to provide feedback. We usually respond if your request is well thought out and asks specific questions, but a note asking “feedback, please” usually goes unanswered.
Number of Pages Required
1 page
Look and feel
Each slider illustrates characteristics of the customer's brand and the style your logo design should communicate.

```html
<!DOCTYPE html>
<html lang="en">
<head>
<meta charset="utf-8">
<title>VEO – Skills Training</title>
<link rel="stylesheet" href="https://fonts.googleapis.com/css2?family=Open+Sans:wght@400;600;700;800&display=swap">
<style>
:root{
  --red:#8c0b14;
  --red-dark:#6e0810;
  --navy:#0d1330;
  --ink:#121a3d;
  --muted:#8a8f9c;
  --light:#f6f6f7;
  --white:#fff;
}
*{box-sizing:border-box;margin:0;padding:0}
html,body{width:1200px;height:4185px;overflow:hidden}
body{position:relative;font-family:"Open Sans",sans-serif;color:var(--ink);background:var(--white)}
.abs{position:absolute}
.ph{position:absolute}

/* header */
.topbar{left:470px;top:0;width:730px;height:30px;background:var(--red);clip-path:polygon(0 0,100% 0,100% 100%,24px 100%);color:#fff;font-size:11px;font-weight:600;display:flex;align-items:center;gap:34px;padding-left:115px}
.topbar span{display:flex;align-items:center;gap:9px}
.ico-dot{width:20px;height:20px;border:1.5px solid #fff;border-radius:50%;display:inline-block}
.header{left:0;top:30px;width:1200px;height:59px}
.logo{position:absolute;left:128px;top:-12px;font-size:54px;font-weight:800;color:var(--red);letter-spacing:-2px;line-height:1}
.nav{position:absolute;left:486px;top:26px;display:flex;gap:0;font-size:11px;font-weight:600}
.nav a{color:var(--ink);text-decoration:none;margin-right:48px}
.nav a.active{color:var(--red);position:relative}
.nav a.active::after{content:"";position:absolute;left:-8px;right:-8px;top:30px;height:3px;background:var(--red)}
.socials{position:absolute;left:908px;top:20px;display:flex;gap:13px}
.socials i{width:24px;height:24px;border:1.5px solid #2a3a8a;border-radius:50%;display:block}

/* hero */
.hero{left:0;top:89px;width:1200px;height:723px;background:linear-gradient(90deg,#050608 0%,#1a1d22 35%,#5b6068 60%,#6e6a62 80%,#3a3c40 100%)}
.hero-tag{left:122px;top:280px;width:266px;height:44px;background:#101a3b;border-left:4px solid var(--red);color:#fff;font-size:21px;font-weight:700;padding:8px 0 0 20px}
.hero-title{left:114px;top:326px;font-size:66px;line-height:86px;font-weight:700;color:#fff;letter-spacing:.5px;white-space:nowrap}
.hero-text{left:122px;top:424px;width:440px;color:#fff;font-size:17px;line-height:26px}
.btn{background:var(--red);color:#fff;font-weight:700;display:flex;align-items:center;justify-content:center}
.hero-btn{left:122px;top:522px;width:175px;height:51px;font-size:16px}
.hero-wave{left:0;top:690px}

/* about */
.about-img{left:227px;top:877px;width:309px;height:455px;background:linear-gradient(180deg,#e8e8ea,#2a2b30 70%,#f0f0f0)}
.eyebrow{font-size:12px;font-weight:600;color:var(--red);text-transform:uppercase;text-decoration:underline;text-underline-offset:4px}
.about .eyebrow{left:610px;top:902px}
.h2{font-size:37px;font-weight:700;color:var(--ink);line-height:46px}
.about .h2{left:610px;top:932px;width:500px}
.about h3{position:absolute;left:610px;top:1052px;font-size:19px;font-weight:600}
.p-muted{font-size:12px;color:var(--muted);line-height:19.5px}
.about .p1{left:610px;top:1091px;width:460px}
.about .p2{left:610px;top:1159px;width:460px}
.about .btn{left:610px;top:1223px;width:136px;height:39px;font-size:14px;gap:10px}

/* services */
.services-bg{left:0;top:1332px;width:1200px;height:552px;background:linear-gradient(180deg,#2a2826,#3a342e 50%,#1f1e1e)}
.services .eyebrow{left:0;width:1200px;text-align:center;top:1397px;color:#fff;text-decoration:none}
.services .eyebrow::after{content:"";display:block;width:92px;height:2px;background:#fff;margin:6px auto 0}
.services .h2{left:0;width:1200px;text-align:center;top:1430px;color:#fff;font-size:42px}
.card{position:absolute;background:#fff;text-align:center;padding-top:28px}
.card .circle{width:84px;height:84px;border-radius:50%;background:var(--red);margin:0 auto;display:flex;align-items:center;justify-content:center}
.card h4{margin-top:25px;font-size:18px;font-weight:700}
.card p{margin:13px auto 0;width:210px;font-size:13px;color:var(--muted);line-height:21px}
.card.featured{background:rgba(140,11,20,.9);color:#fff}
.card.featured .circle{background:#fff}
.card.featured p{color:#fff}

/* why */
.why-bg{left:0;top:1884px;width:1200px;height:636px;background:var(--light)}
.why-img{left:203px;top:1924px;width:333px;height:596px;background:linear-gradient(180deg,#3a2a22 0%,#a88a70 35%,#c9b8a4 60%,#ede8df 100%)}
.why .eyebrow{left:615px;top:1982px}
.why .h2{left:615px;top:2015px;font-size:42px;line-height:51px;width:560px}
.feature{position:absolute;width:218px;height:98px;background:#fff;box-shadow:0 2px 10px rgba(0,0,0,.05);padding:16px 0 0 66px}
.feature svg{position:absolute;left:18px;top:18px}
.feature h5{font-size:15px;font-weight:700;color:#5a6a80}
.feature p{font-size:12px;color:var(--muted);line-height:20px;margin-top:5px}

/* appointment */
.appt-bg{left:0;top:2520px;width:1200px;height:484px;background:linear-gradient(90deg,#0e1014,#23252a 50%,#3a3a3c)}
.appt-img{left:698px;top:2470px;width:502px;height:534px;background:linear-gradient(180deg,#2c2624 0%,#3d3a3c 40%,#20242e 100%)}
.appt h2{position:absolute;left:130px;top:2612px;font-size:33px;font-weight:700;color:#fff}
.field{position:absolute;width:232px;height:43px;background:#fff;font-size:13px;color:#333;display:flex;align-items:center;gap:8px;padding-left:16px}
.field.msg{height:110px;align-items:flex-start;padding-top:12px}
.appt .btn{left:131px;top:2883px;width:131px;height:37px;font-size:12px;font-weight:600;gap:6px}
.appt-wave{left:0;top:2940px}

/* steps */
.steps .eyebrow{left:0;width:1200px;text-align:center;top:3153px}
.steps .h2{left:0;width:1200px;text-align:center;top:3190px;font-size:42px}
.step{position:absolute;width:220px;height:262px;text-align:center}
.step .ring{position:absolute;left:0;top:52px;width:220px;height:220px;border-radius:50%;background:#fff;box-shadow:0 6px 18px rgba(0,0,0,.1)}
.step .top{position:absolute;left:53px;top:0;width:114px;height:114px;border-radius:50%;background:var(--red);display:flex;align-items:center;justify-content:center;box-shadow:0 0 0 10px #fff}
.step .num{position:absolute;left:0;width:220px;top:128px;font-size:13px;font-weight:700;color:var(--red)}
.step h6{position:absolute;left:0;width:220px;top:155px;font-size:14px;font-weight:700;color:#1b6a8a}
.step p{position:absolute;left:20px;width:180px;top:180px;font-size:10px;line-height:13px;color:#333}
.step .more{position:absolute;left:0;width:220px;top:245px;font-size:9px;font-weight:600;color:#1b6a8a}
.step.active .ring{background:var(--red)}
.step.active .top{background:#fff}
.step.active .num,.step.active h6,.step.active p,.step.active .more{color:#fff}

/* footer */
.footer-wave{left:0;top:3680px}
.footer-bg{left:0;top:3784px;width:1200px;height:341px;background:var(--navy)}
.footer-logo{left:0;width:1200px;text-align:center;top:3818px;font-size:84px;font-weight:800;color:#fff;letter-spacing:-3px}
.footer-nav{left:0;width:1200px;top:3944px;display:flex;justify-content:center;gap:48px;font-size:15px;color:#fff}
.footer-line{left:141px;top:3995px;width:918px;height:1px;background:#3a4060}
.contact{position:absolute;top:4040px;display:flex;align-items:center;gap:16px;color:#fff;font-size:12px;line-height:18px}
.contact .ci{width:58px;height:58px;border:1.5px solid #fff;border-radius:50%;display:flex;align-items:center;justify-content:center}
.divider{position:absolute;top:4040px;width:1px;height:60px;background:#555a75}
.bottom-bar{left:0;top:4125px;width:1200px;height:60px;background:var(--red);color:#fff;font-size:13px}
.bottom-bar .brand{position:absolute;left:137px;top:20px}
.bottom-bar .sq{position:absolute;top:18px;width:26px;height:26px;border:1.5px solid #fff}
</style>
</head>
<body>

<!-- header -->
<div class="abs topbar"><span><i class="ico-dot"></i>CALL US TODAY : (123) 456-7890</span><span><i class="ico-dot"></i>EMAIL: info@company.com</span></div>
<header class="abs header">
  <div class="logo">VEO</div>
  <nav class="nav"><a class="active">HOME</a><a>Solutions</a><a>About Us</a><a>Giving Back</a><a>Login</a></nav>
  <div class="socials"><i></i><i></i><i></i><i></i></div>
</header>

<!-- hero -->
<section class="hero-wrap">
  <div class="ph hero" role="img" aria-label="Photo of a smiling man in a wheelchair working on a laptop with a colleague in a modern office"></div>
  <div class="abs hero-tag">We are experts in</div>
  <h1 class="abs hero-title">Skills Training</h1>
  <p class="abs hero-text">Lorem ipsum dolor sit amet, consectetur adipiscing elit, sed do eiusmod tempor incididunt ut labore et dolore magna aliqua.</p>
  <div class="abs btn hero-btn">Read More</div>
  <svg class="abs hero-wave" width="1200" height="125" viewBox="0 0 1200 125">
    <path d="M0 30 C300 110 700 120 1200 20 L1200 125 L0 125 Z" fill="#fff"/>
    <path d="M0 40 C320 120 760 110 1200 6 L1200 30 C760 118 320 128 0 46 Z" fill="#8c0b14"/>
    <path d="M0 34 C330 122 780 105 1200 -4 L1200 4 C780 112 330 130 0 38 Z" fill="#8c0b14" opacity=".6"/>
  </svg>
</section>

<!-- about -->
<section class="about">
  <div class="ph about-img" role="img" aria-label="Photo of business people in suits shaking hands"></div>
  <div class="abs eyebrow">Who we are</div>
  <h2 class="abs h2">New Perspective for a Better Life</h2>
  <h3>Empowerment through Opportunity and Inclusion</h3>
  <p class="abs p-muted p1">Lorem ipsum dolor sit amet, consectetur adipiscing elit, sed do eiusmod temp or incididunt ut labore et dolore magna aliqua. Ut enim ad minim veniam, quis laboris nisi ut aliquip ex ea commodo consequat.</p>
  <p class="abs p-muted p2">Lorem ipsum dolor sit amet, consectetur adipiscing elit, sed do eiusmod temp or incididunt ut labore et dolore magna aliqua.</p>
  <div class="abs btn">Contact us
    <svg width="16" height="12" viewBox="0 0 16 12"><path d="M1 6h13M9 1l5 5-5 5" stroke="#fff" stroke-width="1.6" fill="none"/></svg></div>
</section>

<!-- services -->
<section class="services">
  <div class="ph services-bg" role="img" aria-label="Dimmed photo of a team working together in an office"></div>
  <svg class="abs" style="left:0;top:1330px" width="1200" height="70" viewBox="0 0 1200 70"><path d="M0 0 H1200 V70 C900 0 300 0 0 70 Z" fill="#fff"/></svg>
  <div class="abs eyebrow">Our services</div>
  <h2 class="abs h2">Services We Provide</h2>
  <div class="card" style="left:164px;top:1536px;width:290px;height:267px">
    <div class="circle"><svg width="40" height="40" viewBox="0 0 40 40" fill="none" stroke="#fff" stroke-width="2"><path d="M8 30a14 14 0 1 1 24 0"/><path d="M20 22l5-8"/><circle cx="20" cy="23" r="2"/></svg></div>
    <h4>Skills Training</h4><p>Lorem ipsum dolor sit amet, con sectetur adipiscing elit, sed do eiusmod tem</p></div>
  <div class="card featured" style="left:453px;top:1518px;width:288px;height:302px;padding-top:46px">
    <div class="circle"><svg width="40" height="40" viewBox="0 0 40 40" fill="none" stroke="#8c0b14" stroke-width="2"><path d="M20 8l11 8-4 13H13L9 16z"/><circle cx="20" cy="8" r="3" fill="#fff"/><circle cx="31" cy="16" r="3" fill="#fff"/><circle cx="9" cy="16" r="3" fill="#fff"/></svg></div>
    <h4>Wellness Programs</h4><p>Lorem ipsum dolor sit amet, con sectetur adipiscing elit, sed do eiusmod tem</p></div>
  <div class="card" style="left:741px;top:1536px;width:284px;height:267px">
    <div class="circle"><svg width="40" height="40" viewBox="0 0 40 40" fill="none" stroke="#fff" stroke-width="2"><path d="M10 32h20M14 28l6-16 6 4-6 12"/><circle cx="22" cy="10" r="3"/></svg></div>
    <h4>Job Placement</h4><p>Lorem ipsum dolor sit amet, con sectetur adipiscing elit, sed do eiusmod tem</p></div>
</section>

<!-- why choose us -->
<section class="why">
  <div class="ph why-bg"></div>
  <div class="ph why-img" role="img" aria-label="Photo of a smiling woman in a checked blazer holding a tablet"></div>
  <div class="abs eyebrow">Why choose us</div>
  <h2 class="abs h2">Navigating Challenges, Unlocking Opportunities</h2>
  <div class="feature" style="left:602px;top:2148px"><svg width="32" height="32" viewBox="0 0 32 32" fill="none" stroke="#8c0b14" stroke-width="1.6"><path d="M4 28h22M8 24l6-14 6 4-6 10"/><circle cx="16" cy="7" r="3"/></svg><h5>Confidentiality</h5><p>Inventore veritasis uas vitae dicta sunt</p></div>
  <div class="feature" style="left:848px;top:2148px"><svg width="32" height="32" viewBox="0 0 32 32" fill="none" stroke="#8c0b14" stroke-width="1.6"><path d="M4 28h22M8 24l6-14 6 4-6 10"/><circle cx="16" cy="7" r="3"/></svg><h5>Client-centric</h5><p>Inventore veritasis uas vitae dicta sunt</p></div>
  <div class="feature" style="left:602px;top:2273px"><svg width="32" height="32" viewBox="0 0 32 32" fill="none" stroke="#8c0b14" stroke-width="1.6"><path d="M4 28h22M8 24l6-14 6 4-6 10"/><circle cx="16" cy="7" r="3"/></svg><h5>Professionalism</h5><p>Inventore veritasis uas vitae dicta sunt</p></div>
  <div class="feature" style="left:848px;top:2273px"><svg width="32" height="32" viewBox="0 0 32 32" fill="none" stroke="#8c0b14" stroke-width="1.6"><path d="M4 28h22M8 24l6-14 6 4-6 10"/><circle cx="16" cy="7" r="3"/></svg><h5>Proven Record</h5><p>Inventore veritasis uas vitae dicta sunt</p></div>
</section>

<!-- appointment -->
<section class="appt">
  <div class="ph appt-bg" role="img" aria-label="Dimmed office background photo"></div>
  <div class="ph appt-img" role="img" aria-label="Photo of a smiling businessman and businesswoman standing with arms crossed"></div>
  <h2>Request An Appointment</h2>
  <div class="field" style="left:132px;top:2686px">&#9786; Full Name</div>
  <div class="field" style="left:390px;top:2686px">&#9993; Email Address</div>
  <div class="field" style="left:132px;top:2753px">&#9742; Phone</div>
  <div class="field msg" style="left:390px;top:2753px">&#9993; Message</div>
  <div class="field" style="left:132px;top:2821px">&#9719; Date</div>
  <div class="abs btn">Request Now
    <svg width="12" height="10" viewBox="0 0 12 10"><path d="M1 5h9M6 1l4 4-4 4" stroke="#fff" stroke-width="1.4" fill="none"/></svg></div>
  <svg class="abs appt-wave" width="1200" height="70" viewBox="0 0 1200 70"><path d="M0 20 C300 80 900 80 1200 10 V70 H0 Z" fill="#fff"/></svg>
</section>

<!-- steps -->
<section class="steps">
  <div class="abs eyebrow">Steps to take</div>
  <h2 class="abs h2">Steps to Take</h2>
  <div class="step" style="left:122px;top:3293px"><div class="ring"></div><div class="top"><svg width="44" height="44" viewBox="0 0 32 32" fill="none" stroke="#fff" stroke-width="1.5"><path d="M4 28h22M8 24l6-14 6 4-6 10"/><circle cx="16" cy="7" r="3"/></svg></div><div class="num">1</div><h6>Get in touch with us</h6><p>Lorem ipsum dolor sit amet, con sectetur adipiscing elit, sed do eiusmod tempor incididunt ut labore et dol ore magna aliqua. Ut</p><div class="more">Read More</div></div>
  <div class="step active" style="left:366px;top:3293px"><div class="ring"></div><div class="top"><svg width="44" height="44" viewBox="0 0 40 40" fill="none" stroke="#8c0b14" stroke-width="2"><path d="M20 8l11 8-4 13H13L9 16z"/></svg></div><div class="num">2</div><h6>Speak to an Expert</h6><p>Lorem ipsum dolor sit amet, con sectetur adipiscing elit, sed do eiusmod tempor incididunt ut labore et dol ore magna aliqua. Ut</p><div class="more">Read More</div></div>
  <div class="step" style="left:613px;top:3293px"><div class="ring"></div><div class="top"><svg width="44" height="44" viewBox="0 0 40 40" fill="none" stroke="#fff" stroke-width="2"><path d="M8 30a14 14 0 1 1 24 0"/><path d="M20 22l5-8"/></svg></div><div class="num">3</div><h6>Schedule a meeting</h6><p>Lorem ipsum dolor sit amet, con sectetur adipiscing elit, sed do eiusmod tempor incididunt ut labore et dol ore magna aliqua. Ut</p><div class="more">Read More</div></div>
  <div class="step" style="left:858px;top:3293px"><div class="ring"></div><div class="top"><svg width="44" height="44" viewBox="0 0 40 40" fill="none" stroke="#fff" stroke-width="2"><circle cx="18" cy="18" r="12"/><circle cx="27" cy="27" r="5"/></svg></div><div class="num">4</div><h6>Start Sessions</h6><p>Lorem ipsum dolor sit amet, con sectetur adipiscing elit, sed do eiusmod tempor incididunt ut labore et dol ore magna aliqua. Ut</p><div class="more">Read More</div></div>
</section>

<!-- footer -->
<footer>
  <svg class="abs footer-wave" width="1200" height="110" viewBox="0 0 1200 110">
    <path d="M0 104 C300 0 800 -10 1200 60 V110 H0 Z" fill="#0d1330"/>
    <path d="M0 90 C300 -12 800 -20 1200 50 V62 C800 -6 300 2 0 100 Z" fill="#8c0b14"/>
    <path d="M0 80 C300 -22 800 -30 1200 38 V44 C800 -22 300 -14 0 86 Z" fill="#8c0b14" opacity=".7"/>
  </svg>
  <div class="ph footer-bg"></div>
  <div class="abs footer-logo">VEO</div>
  <div class="abs footer-nav"><span>HOME</span><span>SERVICES</span><span>ABOUT US</span><span>TESTIMONIALS</span><span>BLOG</span></div>
  <div class="abs footer-line"></div>
  <div class="contact" style="left:141px"><div class="ci"><svg width="30" height="30" viewBox="0 0 30 30" fill="none" stroke="#fff" stroke-width="1.4"><circle cx="15" cy="15" r="11"/><path d="M4 15h22M15 4c-5 6-5 16 0 22M15 4c5 6 5 16 0 22"/></svg></div><div>123, Building Name, Street<br>City, State XY 123456</div></div>
  <div class="divider" style="left:398px"></div>
  <div class="contact" style="left:474px"><div class="ci"><svg width="30" height="30" viewBox="0 0 30 30" fill="none" stroke="#fff" stroke-width="1.4"><rect x="9" y="4" width="12" height="22" rx="2"/></svg></div><div>PHONE<br>(123) 456 7890</div></div>
  <div class="divider" style="left:718px"></div>
  <div class="contact" style="left:795px"><div class="ci"><svg width="30" height="30" viewBox="0 0 30 30" fill="none" stroke="#fff" stroke-width="1.4"><rect x="5" y="9" width="20" height="14"/><path d="M5 9l10 8 10-8"/></svg></div><div>EMAIL<br>info@company.com</div></div>
  <div class="abs bottom-bar"><span class="brand">VEO</span>
    <i class="sq" style="left:932px"></i><i class="sq" style="left:965px"></i><i class="sq" style="left:998px"></i><i class="sq" style="left:1031px"></i></div>
</footer>

</body>
</html>
```